KLP Ad to drive teacher course enrollment

I need a relatively simple ad that is a color 4.75" w X 6" h PDF. I am attaching a poorly designed sample that I put together with the appropriate text, our branding guidelines, and a sample of a more polished ad (not ours) that appeared in the same publication for reference. I am also attaching our logo file and a couple of possible photos. We can include one photo or no photo, but not two photos. If you would like some other photo options please let me know.

Requirements
Must have
• Our logo, the dates and enrollment address as a focus, must keep the headline sentences together "Advance your students' thinking through writing" "Learn to embed the Varsley Method in any subject"
Nice to have
• Clean design, white space
Should not have
• Images blocking words, too many color text

```html
<!DOCTYPE html>
<html lang="en">
<head>
<meta charset="utf-8">
<title>KLP Course Enrollment Ad</title>
<link rel="stylesheet" href="https://fonts.googleapis.com/css2?family=Lato:wght@400;700;900&display=swap">
<style>
  :root {
    --brand-blue: #1b5aa6;
    --brand-orange: #ef8a22;
    --brand-red: #d6232e;
    --brand-purple: #5b2a6e;
    --ink-grey: #3c3c3c;
    --paper: #ffffff;
    --backdrop: #d9d9d9;
    --photo-deep: #3d5f93;
    --photo-light: #b9c9df;
  }
  * { box-sizing: border-box; margin: 0; padding: 0; }
  html, body { width: 800px; height: 1200px; overflow: hidden; }
  body {
    background: var(--backdrop);
    font-family: "Lato", Arial, sans-serif;
    position: relative;
  }
  .ad {
    position: absolute;
    left: 0; top: 97px;
    width: 800px; height: 1006px;
    background: var(--paper);
    overflow: hidden;
  }
  .ad-shapes { position: absolute; inset: 0; }
  .headline {
    position: absolute; top: 38px; left: 10px; right: 10px;
    text-align: center;
    color: var(--brand-blue);
    font-weight: 900;
    font-size: 28px;
    line-height: 35px;
    text-transform: uppercase;
    white-space: nowrap;
  }
  .registration {
    position: absolute; top: 604px; left: 0; right: 0;
    text-align: center; color: var(--paper);
  }
  .registration-title { font-size: 27px; font-weight: 400; letter-spacing: 0.3px; }
  .registration-rule {
    width: 72px; height: 3px; background: var(--paper);
    margin: 6px auto 14px;
  }
  .registration-details { font-size: 20px; line-height: 25px; }
  .enroll-line {
    position: absolute; top: 719px; left: 132px; width: 546px; height: 40px;
    display: flex; align-items: center; justify-content: center;
    color: var(--paper); font-size: 23px;
  }
  .enroll-line strong { font-weight: 900; margin-left: 6px; }
  .register-note {
    position: absolute; top: 771px; left: 0; right: 0;
    text-align: center; font-size: 20px; color: var(--brand-purple);
  }
  .register-note .register-word { color: var(--brand-red); font-size: 25px; margin-right: 6px; }
  .discount-text {
    position: absolute; top: 806px; left: 36px; height: 58px;
    display: flex; align-items: center;
    color: var(--paper); font-size: 42px; font-weight: 700;
  }
  .code-text {
    position: absolute; top: 806px; left: 552px; height: 58px;
    display: flex; align-items: center;
    color: var(--paper); font-size: 42px; font-weight: 700;
  }
  .provider-note {
    position: absolute; top: 906px; left: 32px;
    color: var(--brand-blue); font-size: 20px; font-weight: 700;
    line-height: 25px; text-transform: uppercase;
  }
  .footer-divider {
    position: absolute; left: 450px; top: 886px;
    width: 2px; height: 102px; background: var(--brand-blue);
  }
  .brand-mark {
    position: absolute; top: 898px; left: 494px;
    display: flex; align-items: center; gap: 12px;
  }
  .brand-dot { width: 20px; height: 20px; border-radius: 50%; background: var(--brand-blue); }
  .brand-name {
    color: var(--brand-blue); font-size: 27px; font-weight: 400;
    line-height: 30px; text-transform: uppercase;
  }
  .brand-tagline {
    position: absolute; top: 964px; left: 494px;
    color: var(--ink-grey); font-size: 15px;
  }
</style>
</head>
<body>
  <main class="ad">
    <svg class="ad-shapes" width="800" height="1006" viewBox="0 0 800 1006">
      <defs>
        <linearGradient id="classroomTone" x1="0" y1="0" x2="1" y2="1">
          <stop offset="0" stop-color="var(--photo-light)"/>
          <stop offset="0.55" stop-color="var(--photo-deep)"/>
          <stop offset="1" stop-color="#d9dde6"/>
        </linearGradient>
      </defs>
      <polygon class="classroom-photo" role="img" aria-label="Photo of a smiling student at her desk with a teacher leaning in to help"
        points="0,158 400,212 800,136 800,620 0,640" fill="url(#classroomTone)"/>
      <polygon class="accent-stripe" points="420,208 800,126 800,146 470,216" fill="var(--brand-orange)"/>
      <polygon class="accent-stripe" points="0,600 560,540 600,548 0,618" fill="var(--brand-orange)"/>
      <polygon class="registration-band" points="0,622 600,548 800,590 800,745 0,745" fill="var(--brand-blue)"/>
      <polygon class="enroll-bar" points="150,717 678,717 660,759 132,759" fill="var(--brand-red)"/>
      <polygon class="discount-bar" points="0,806 540,806 522,864 0,864" fill="var(--brand-orange)"/>
      <polygon class="code-bar" points="540,806 800,806 800,864 522,864" fill="var(--brand-purple)"/>
      <line x1="540" y1="806" x2="522" y2="864" stroke="var(--paper)" stroke-width="4"/>
    </svg>

    <h1 class="headline">Advance your students’ thinking through<br>writing Learn to embed the Varsley<br>Method into any subject</h1>

    <section class="registration">
      <h2 class="registration-title">COURSE REGISTRATION</h2>
      <div class="registration-rule"></div>
      <p class="registration-details">Foundations of Analytical Writing I (Grades 3-12)<br>Next Courses Begin: October 12 and December 12th</p>
    </section>

    <p class="enroll-line">Enroll at <strong>kestrellearning.org/courses</strong></p>
    <p class="register-note"><span class="register-word">Register</span>Early Before Courses Reach Capacity</p>

    <p class="discount-text">10% Discount with the</p>
    <p class="code-text">Code: EDU</p>

    <p class="provider-note">Kestrel Learning Press is an<br>approved provider of CTLE credits.</p>
    <div class="footer-divider"></div>
    <div class="brand-mark">
      <span class="brand-dot"></span>
      <span class="brand-name">Kestrel<br>Learning Press</span>
    </div>
    <p class="brand-tagline">Clear Writing, Deeper Thinking</p>
  </main>
</body>
</html>
```